Brookmere Osteopathy flyer

I want a clean clear DL flyer (but also want an A4 poster) promoting a new Osteopathic business in a semi rural area in Tasmania (Australia).
It can have pictures like the examples attached to show people what Osteopathy is (its like Chiropractic and physiotherapy).
I am the sole practioner and am male, so any pictures would be best to be a white male if possible.
I've attached some wording, you can use all, or none of it
I don't have a phone number for the business yet
info@brookmereosteopathy.example
www.brookmereosteopathy.example
Target Market(s)
Australians, from tradies, professionals, babies to retired people
Industry/Entity Type
Health
Look and feel

```html
<!DOCTYPE html>
<html lang="en">
<head>
<meta charset="utf-8">
<title>Brookmere Osteopathy – DL Flyer</title>
<link rel="stylesheet" href="https://fonts.googleapis.com/css2?family=Bebas+Neue&family=Poppins:wght@400;600&display=swap">
<style>
  :root{
    --orange:#f39237;
    --blue:#2f8fd4;
    --navy:#1d5f96;
    --ink:#231f20;
    --paper:#ffffff;
    --stage:#6f6f6f;
  }
  *{margin:0;padding:0;box-sizing:border-box}
  html,body{width:1200px;height:574px;overflow:hidden}
  body{background:var(--stage);position:relative;font-family:"Poppins",sans-serif;color:var(--ink)}
  .flyer{position:absolute;top:32px;width:248px;height:511px;background:var(--paper);overflow:hidden;box-shadow:0 4px 14px rgba(0,0,0,.35)}
  .flyer--front{left:346px}
  .flyer--back{left:606px}
  .flyer__art{position:absolute;inset:0;width:248px;height:511px}

  .brand{position:absolute;left:20px;top:22px;display:flex;align-items:center;gap:10px}
  .brand__dot{width:56px;height:56px;border-radius:50%;border:2px solid var(--blue);flex:none}
  .brand__name{font-family:"Bebas Neue",sans-serif;font-size:31px;line-height:28px;color:var(--ink);letter-spacing:.5px}

  .reasons-title{position:absolute;left:21px;top:226px;width:206px;height:33px;background:var(--ink);color:#fff;text-align:center;font-size:11px;line-height:13.5px;padding-top:3px}
  .reasons-title strong{color:var(--orange);font-weight:600}

  .reasons{position:absolute;top:281px;list-style:none;font-size:9.4px;line-height:10.6px}
  .reasons--left{left:21px;width:110px}
  .reasons--right{left:131px;width:110px}
  .reasons li{position:relative;padding-left:11px;margin-bottom:4px}
  .reasons li::before{content:"";position:absolute;left:0;top:2px;width:7px;height:7px;border-radius:50%;background:var(--orange)}
  .reasons li::after{content:"";position:absolute;left:2.2px;top:3.4px;width:2px;height:3.2px;border:solid #fff;border-width:0 1.2px 1.2px 0;transform:rotate(45deg)}

  .web{position:absolute;left:0;right:0;top:476px;text-align:center;color:#fff;font-size:9.5px}
  .flyer--back .web{text-align:left;padding-left:28px}

  .badge{position:absolute;left:96px;top:222px;width:56px;display:flex;flex-direction:column;align-items:center;gap:3px}
  .badge__dot{width:52px;height:52px;border-radius:50%;border:2px solid var(--blue);background:#fff}
  .badge__name{font-size:5.6px;color:var(--blue);white-space:nowrap;font-weight:600}

  .about{position:absolute;left:21px;top:278px;width:206px;font-size:8.6px;line-height:12.3px;text-align:justify}
  .contact-title{position:absolute;left:21px;top:336px;width:206px;height:22px;background:var(--ink);color:#fff;text-align:center;font-size:11.5px;line-height:22px}
  .contact{position:absolute;left:33px;top:364px;list-style:none;font-size:9.8px;line-height:15.6px}
  .contact li{display:flex;align-items:center;gap:8px}
  .contact svg{width:9px;height:9px;flex:none}
</style>
</head>
<body>

<section class="flyer flyer--front">
  <svg class="flyer__art" viewBox="0 0 248 511" aria-hidden="false">
    <defs>
      <linearGradient id="frontPhoto" x1="0" y1="0" x2="1" y2="1">
        <stop offset="0" stop-color="#eef1f3"/><stop offset=".55" stop-color="#d9d3cd"/><stop offset="1" stop-color="#c6ccd2"/>
      </linearGradient>
      <linearGradient id="frontLower" x1="0" y1="0" x2="0" y2="1">
        <stop offset="0" stop-color="#ffffff"/><stop offset=".5" stop-color="#e6ddd6"/><stop offset="1" stop-color="#cdb9aa"/>
      </linearGradient>
    </defs>
    <g role="img" aria-label="Practitioner stretching a patient's arm and shoulder on a treatment table">
      <polygon points="0,92 248,92 248,285 0,178" fill="url(#frontPhoto)"/>
    </g>
    <line x1="0" y1="178" x2="248" y2="286" stroke="var(--orange)" stroke-width="3"/>
    <g role="img" aria-label="Hands massaging a patient's lower back">
      <rect x="0" y="375" width="248" height="136" fill="url(#frontLower)"/>
    </g>
    <polygon points="0,452 248,422 248,511 0,511" fill="var(--blue)" opacity=".88"/>
    <polygon points="0,452 78,511 0,511" fill="var(--orange)"/>
  </svg>

  <header class="brand">
    <span class="brand__dot"></span>
    <h1 class="brand__name">Brookmere<br>Osteopathy</h1>
  </header>

  <h2 class="reasons-title">Common Reasons People<br>Visit an <strong>Osteopath:</strong></h2>

  <ul class="reasons reasons--left">
    <li>Back / Neck Pain</li>
    <li>Headaches /<br>Migraines</li>
    <li>Joint &amp; Muscle Pain</li>
    <li>Pregnancy-related Discomfort</li>
    <li>Disc Related Issues</li>
  </ul>
  <ul class="reasons reasons--right">
    <li>Sciatica</li>
    <li>Plantar Fasciitis</li>
    <li>Tendonitis / Bursitis</li>
    <li>Adhesive Capsulitis (Frozen Shoulder)</li>
    <li>Tennis / Golfers Elbow</li>
  </ul>

  <p class="web">www.brookmereosteopathy.example</p>
</section>

<section class="flyer flyer--back">
  <svg class="flyer__art" viewBox="0 0 248 511">
    <defs>
      <linearGradient id="backTop" x1="0" y1="0" x2="1" y2="1">
        <stop offset="0" stop-color="#eceff1"/><stop offset=".6" stop-color="#d9b89c"/><stop offset="1" stop-color="#c99f80"/>
      </linearGradient>
      <linearGradient id="backBaby" x1="0" y1="0" x2="1" y2="0">
        <stop offset="0" stop-color="#1d5f96"/><stop offset="1" stop-color="#3a9be0"/>
      </linearGradient>
      <linearGradient id="backLower" x1="0" y1="0" x2="0" y2="1">
        <stop offset="0" stop-color="#ffffff"/><stop offset=".5" stop-color="#e4dad2"/><stop offset="1" stop-color="#cbb6a6"/>
      </linearGradient>
    </defs>
    <g role="img" aria-label="Practitioner's hands treating a patient's upper back">
      <polygon points="0,0 248,0 248,170 0,74" fill="url(#backTop)"/>
    </g>
    <line x1="0" y1="74" x2="248" y2="170" stroke="var(--orange)" stroke-width="3"/>
    <g role="img" aria-label="Gentle cranial treatment for a sleeping baby">
      <polygon points="0,74 248,170 248,262 118,206 0,168" fill="url(#backBaby)"/>
    </g>
    <g role="img" aria-label="Practitioner supporting a woman's head and neck">
      <polygon points="0,168 118,206 0,280" fill="#d8d4d2"/>
    </g>
    <line x1="0" y1="168" x2="118" y2="206" stroke="var(--orange)" stroke-width="2.5"/>
    <line x1="0" y1="281" x2="118" y2="206" stroke="var(--orange)" stroke-width="2.5"/>
    <line x1="118" y1="206" x2="248" y2="263" stroke="var(--orange)" stroke-width="2.5"/>
    <g role="img" aria-label="Hands massaging a patient's back">
      <rect x="0" y="410" width="248" height="101" fill="url(#backLower)"/>
    </g>
    <polygon points="0,432 248,488 248,511 0,511" fill="var(--navy)" opacity=".85"/>
    <polygon points="167,511 248,453 248,511" fill="var(--orange)"/>
  </svg>

  <div class="badge">
    <span class="badge__dot"></span>
  </div>

  <p class="about">Osteopaths use a combination of joint manipulation, targeted deep tissue massage and stretching to improve function, relieve pain and support the body’s ability to heal itself.</p>

  <h2 class="contact-title">Contact Us:</h2>
  <ul class="contact">
    <li><svg viewBox="0 0 10 10"><path d="M5 0.5a3.3 3.3 0 0 0-3.3 3.3C1.7 6.3 5 9.6 5 9.6s3.3-3.3 3.3-5.8A3.3 3.3 0 0 0 5 .5zm0 4.6a1.3 1.3 0 1 1 0-2.6 1.3 1.3 0 0 1 0 2.6z" fill="var(--orange)"/></svg>24 Mill Lane, Brookmere</li>
    <li><svg viewBox="0 0 10 10"><path d="M2.2 .8l1.6 2-1 1.1c.6 1.3 1.6 2.3 2.9 2.9l1.1-1 2 1.6-.9 1.6C4.6 9 1 5.4.6 1.7z" fill="var(--orange)"/></svg>+00 111 222 333</li>
    <li><svg viewBox="0 0 10 10"><rect x=".5" y="2" width="9" height="6.2" fill="var(--orange)"/><path d="M.8 2.3L5 5.6l4.2-3.3" fill="none" stroke="#fff" stroke-width=".8"/></svg>info@brookmereosteopathy.example</li>
  </ul>

  <p class="web">www.brookmereosteopathy.example</p>
</section>

</body>
</html>
```